International IT business needs website revamp.

Velbric Limited would like their current website (www.velbriclimited.example) to be revamped/modernized to reflect up-to-date goods and services. Currently, Velbric is offering a conversational AI workflow platform for both enterprise clients and as a DIY solution for SMBs. This platform is called tmPilot and allows organizations to automate simple and repetitive workflows to drive their operational efficiency. In addition to the solution offering, Velbric Limited also provides professional IT services. With that said, please use www.velbriclimited.example and www.tmpilot.example for reference of current logos and colourways desired. Furthermore, refer to the attached PDF for a general idea of what to include in the site. The final design should be easy to navigate, clear, concise, and emphasize tmPilot as a solution for enterprise clients (while redirecting SMBs to the tmPilot website) looking to automate workflow processes/kickstart their digital transformation journey.
Updates
Coding
Number of Pages Required
5+ page
Font styles to use
Look and feel
Each slider illustrates characteristics of the customer's brand and the style your logo design should communicate.

```html
<!DOCTYPE html>
<html lang="en">
<head>
<meta charset="utf-8">
<title>Velbric Limited</title>
<link href="https://fonts.googleapis.com/css2?family=Poppins:wght@400;500;600;700&family=Montserrat:wght@500;600;700&display=swap" rel="stylesheet">
<style>
:root{
  --green:#4fd68c;
  --green-dark:#2ec35d;
  --ink:#3f3f46;
  --text:#55575c;
  --muted:#8a8c91;
  --blue:#1aa3e8;
  --night:#0b0d12;
  --light:#f1f1f3;
  --white:#ffffff;
  --star:#f7b42c;
}
*{box-sizing:border-box;margin:0;padding:0}
html,body{width:1200px;height:3288px;overflow:hidden;background:var(--white)}
body{position:relative;font-family:'Poppins',sans-serif;color:var(--text)}
.abs{position:absolute}
.brand{display:flex;align-items:center;gap:6px;font-family:'Poppins',sans-serif;font-weight:500;letter-spacing:.5px}
.brand .mark{border:2px solid currentColor;display:inline-block}
/* hero */
.hero-photo{left:0;top:0;width:1200px;height:562px;background:radial-gradient(ellipse at 78% 35%,#3b4a6a 0%,#1a2340 35%,#0c1224 70%);clip-path:polygon(0 0,1200px 0,1200px 491px,600px 562px,0 491px)}
.nav{top:34px;left:0;width:1200px;height:26px;color:var(--white)}
.nav .brand{position:absolute;left:234px;top:0;font-size:17px;color:var(--white)}
.nav .brand .mark{width:22px;height:22px}
.nav a{position:absolute;top:5px;font-family:'Montserrat',sans-serif;font-weight:600;font-size:10.5px;color:var(--white);text-decoration:none;letter-spacing:.4px}
.nav a.active{border:1.5px solid var(--white);padding:7px 14px;top:0}
.phone{position:absolute;left:817px;top:1px;display:flex;align-items:center;gap:8px;font-family:'Montserrat',sans-serif;font-weight:600;font-size:17px}
.hero-arrow{width:34px;height:34px;border:2px solid var(--white);top:245px;display:flex;align-items:center;justify-content:center}
.product{left:234px;top:178px;display:flex;align-items:center;gap:8px;color:var(--blue);font-size:28px;font-weight:400}
.product .dot{width:42px;height:42px;border-radius:50%;background:var(--blue)}
.hero h1{position:absolute;left:234px;top:234px;font-size:66px;font-weight:700;color:var(--white);letter-spacing:1px;line-height:1}
.hero .sub{position:absolute;left:234px;top:308px;font-size:16.5px;font-weight:600;color:var(--white)}
.btn{position:absolute;height:46px;width:160px;border-radius:23px;background:linear-gradient(90deg,var(--green),var(--green-dark));display:flex;align-items:center;padding-left:24px;gap:14px;color:var(--white);font-family:'Montserrat',sans-serif;font-weight:600;font-size:12.5px}
.btn .sq{width:22px;height:22px;border:2px solid var(--white)}
.pager{top:503px;left:574px;display:flex;gap:8px}
.pager span{width:12px;height:12px;border:2px solid var(--white)}
.pager span.on{background:var(--white)}
/* section heads */
.eyebrow{font-size:12px;letter-spacing:3px;font-weight:500;color:var(--green);font-family:'Montserrat',sans-serif}
.title{font-size:33px;font-weight:700;color:var(--ink)}
.center{left:0;width:1200px;text-align:center}
/* about */
.photo{background:linear-gradient(135deg,#d9dde3,#9aa2ad)}
.about p{position:absolute;left:664px;width:302px;font-size:10.6px;line-height:16.3px;color:var(--text)}
/* services */
.services-bg{left:0;top:1094px;width:1200px;height:548px;background:linear-gradient(180deg,#efeff1,#f6f6f8)}
.hex-text h3{font-size:13.5px;font-weight:600;color:var(--ink);text-align:center}
.hex-text ul{list-style:none;margin-top:12px}
.hex-text li{font-size:9.8px;line-height:15px;color:var(--text);padding-left:11px;position:relative;margin-bottom:4px}
.hex-text li::before{content:"";position:absolute;left:0;top:5px;width:5px;height:5px;border-radius:50%;background:var(--green)}
.icon-circle{width:64px;height:64px;border-radius:50%;background:var(--green);border:4px solid #c9f1db}
/* testimonials */
.card{top:1818px;width:356px;height:292px;background:var(--white);box-shadow:0 2px 10px rgba(0,0,0,.09);padding:22px 28px}
.card .quote{font-size:70px;line-height:.8;color:var(--green);font-weight:700;font-family:Georgia,serif}
.card p{font-size:10.5px;line-height:16.3px;color:var(--text);margin-top:8px}
.card h4{font-size:11.5px;font-weight:600;color:var(--ink);margin-top:16px}
.stars{color:var(--star);font-size:13px;letter-spacing:1px;margin-top:2px}
/* video */
.video{left:0;top:2187px;width:1200px;height:370px;background:linear-gradient(90deg,#6fe09a 0%,#63d891 50%,#5bcf88 100%)}
/* clients */
.logos{display:grid;grid-template-columns:110px 110px;gap:30px 20px;justify-items:center}
.logos span{font-size:24px;font-weight:700;color:#2b4f8f}
.dots{display:flex;gap:4px}
.dots i{width:5px;height:5px;border-radius:50%;background:#d8d8dc}
.dots i.on{background:#a0a0a6}
/* footer */
.footer-bg{left:0;top:2888px;width:1200px;height:400px;background:var(--night);clip-path:polygon(0 87px,600px 0,1200px 87px,1200px 400px,0 400px)}
.foot h5{font-size:11px;font-weight:700;color:var(--white);letter-spacing:.5px;font-family:'Montserrat',sans-serif}
.foot h5::after{content:"";display:block;width:30px;height:2px;background:var(--green);margin-top:8px}
.foot .lnk{font-size:9.8px;color:#e6e6e6;line-height:25px}
.foot p{font-size:9.8px;line-height:15px;color:#e6e6e6}
.social{display:flex;align-items:center;gap:10px;font-size:9.8px;color:#e6e6e6;height:25px}
.social i{width:16px;height:16px;border-radius:50%;background:#2a2d33}
</style>
</head>
<body>

<!-- HERO -->
<section class="hero">
  <div class="abs hero-photo" role="img" aria-label="Woman working on a tablet at night in front of a window with city bokeh lights"></div>
  <nav class="abs nav">
    <div class="brand"><span class="mark"></span>VELBRIC</div>
    <a class="active" style="left:414px">HOME</a>
    <a style="left:484px">SOLUTIONS</a>
    <a style="left:565px">SERVICES</a>
    <a style="left:640px">ABOUT US</a>
    <a style="left:717px">CONTACT US</a>
    <div class="phone">
      <svg width="16" height="16" viewBox="0 0 24 24" fill="#fff"><path d="M6.6 10.8a15.1 15.1 0 0 0 6.6 6.6l2.2-2.2a1 1 0 0 1 1-.25 11.4 11.4 0 0 0 3.6.57 1 1 0 0 1 1 1V20a1 1 0 0 1-1 1A17 17 0 0 1 3 4a1 1 0 0 1 1-1h3.5a1 1 0 0 1 1 1c0 1.25.2 2.45.57 3.57a1 1 0 0 1-.25 1z"/></svg>
      (555) 014-2290
    </div>
  </nav>
  <div class="abs hero-arrow" style="left:101px"><svg width="14" height="18" viewBox="0 0 14 18"><path d="M10 2 3 9l7 7" stroke="#fff" stroke-width="2" fill="none"/></svg></div>
  <div class="abs hero-arrow" style="left:1067px"><svg width="14" height="18" viewBox="0 0 14 18"><path d="M4 2l7 7-7 7" stroke="#fff" stroke-width="2" fill="none"/></svg></div>
  <div class="abs product"><span class="dot"></span>tmPilot</div>
  <h1>COULD IT BE?</h1>
  <div class="sub">Finally, an enterprise chatbot platform that really delivers</div>
  <div class="btn" style="left:234px;top:354px"><span class="sq"></span>LEARN MORE</div>
  <div class="abs pager"><span class="on"></span><span></span><span></span></div>
</section>

<!-- ABOUT -->
<section class="about">
  <div class="abs photo" style="left:234px;top:642px;width:293px;height:291px" role="img" aria-label="Business team standing and talking in a bright office"></div>
  <div class="abs photo" style="left:328px;top:730px;width:281px;height:287px;background:linear-gradient(135deg,#e8ecef,#8b939c)" role="img" aria-label="Colleagues in a meeting around a table"></div>
  <div class="abs eyebrow" style="left:664px;top:640px;display:flex;align-items:center;gap:10px">INTRODUCTION<span style="width:40px;height:2px;background:var(--green)"></span></div>
  <div class="abs title" style="left:664px;top:664px">About Velbric</div>
  <p style="top:720px">Since 2011, the Velbric team has been providing professional IT services for major Canadian corporations operating in the telecommunications and financial sectors. As such, our team is highly skilled in technology integration, legacy modernization, system architecture design, application development, quality assurance, project management and more!</p>
  <p style="top:850px">As of 2017, the Velbric team has developed and launched tmPilot, a conversational workflow platform powered by AI and ML, into production. Our vision for tmPilot is to drive the operational economy, efficiency, and effectiveness of any organization by automating simple and repetitive workflows.</p>
  <div class="btn" style="left:665px;top:971px"><span class="sq"></span>LEARN MORE</div>
</section>

<!-- SERVICES -->
<section>
  <div class="abs services-bg" role="img" aria-label="Faint light grey hexagon pattern background"></div>
  <div class="abs center eyebrow" style="top:1150px">SERVICES</div>
  <div class="abs center title" style="top:1174px">What We Do</div>
  <svg class="abs" style="left:360px;top:1232px" width="480" height="60" viewBox="0 0 480 60"><path d="M217 2v12l-6 10H8v34M263 2v12l6 10h203v34" stroke="#b5b5ba" stroke-dasharray="4 3" fill="none"/></svg>
  <svg class="abs" style="left:250px;top:1284px" width="235" height="270"><polygon points="117,8 227,71 227,198 117,262 8,198 8,71" fill="#fff" stroke="#fff" stroke-width="14" stroke-linejoin="round"/></svg>
  <svg class="abs" style="left:716px;top:1284px" width="235" height="270"><polygon points="117,8 227,71 227,198 117,262 8,198 8,71" fill="#fff" stroke="#fff" stroke-width="14" stroke-linejoin="round"/></svg>
  <div class="abs icon-circle" style="left:334px;top:1322px"></div>
  <div class="abs hex-text" style="left:285px;top:1402px;width:170px">
    <h3>Digital Transformation</h3>
    <ul><li>Process Automation via RPA and Conversational AI</li><li>Enterprise Application Integration</li></ul>
  </div>
  <div class="abs icon-circle" style="left:800px;top:1322px"></div>
  <div class="abs hex-text" style="left:752px;top:1402px;width:165px">
    <h3>Network of Expertise</h3>
    <ul><li>full-stack development,</li><li>from AI/ML and data to legacy</li></ul>
  </div>
  <div class="abs brand" style="left:560px;top:1322px;font-size:16px;color:#111"><span class="mark" style="width:22px;height:22px"></span>VELBRIC</div>
  <p class="abs" style="left:498px;top:1364px;width:204px;text-align:center;font-size:9.6px;line-height:15.1px;color:var(--text)">Contract Staffing: At Velbric, our staff are readily available to deliver experienced and knowledgeable assistance to fill immediate or temporary needs for a diverse range of technologies and positions. Thus, we provide seasoned IT resources with a strong sense of business acumen to bring valuable experience and expertise to our clients to achieve reduced costs, greater efficiency and better services.</p>
  <div class="btn" style="left:520px;top:1537px"><span class="sq"></span>LEARN MORE</div>
</section>

<!-- TESTIMONIALS -->
<section>
  <div class="abs center eyebrow" style="top:1710px">TESTIMONIALS</div>
  <div class="abs center title" style="top:1735px">What Our Clients Are Saying</div>
  <div class="abs card" style="left:234px">
    <div class="quote">&ldquo;</div>
    <p>“Naturally, the Northway Passports website receives thousands of visitors a day. As a result, we noticed the need to automate simple and repetitive questions to provide quick, on-demand assistance while maximizing our worker productivity without compromising costs. Thus, we enlisted Velbric Limited and their tmPilot solution to accomplish the task. Since launching the Northway Passports bot in Q4, 2019, we have achieved over 75% of inquiries being automatically answered successfully!”</p>
    <h4>Northway Passports</h4>
    <div class="stars">★★★★★</div>
  </div>
  <div class="abs card" style="left:610px">
    <div class="quote">&ldquo;</div>
    <p>“Leveraging tmPilot’s extremely user-friendly interface, Civic Services Office was able to build and implement our own bot for the My Civic Account (MCA) page without the assistance of Velbric developers. By removing the need for programmers, we are able to make adjustments to our bot instantaneously!”</p>
    <h4>Civic Services Office</h4>
    <div class="stars">★★★★★</div>
  </div>
</section>

<!-- VIDEO -->
<section>
  <div class="abs video" role="img" aria-label="Green-tinted video still of a woman smiling at her laptop in an office"></div>
  <svg class="abs" style="left:555px;top:2324px" width="96" height="96"><circle cx="48" cy="48" r="45" fill="none" stroke="#fff" stroke-width="3"/><path d="M38 30v36l29-18z" fill="#fff"/></svg>
  <div class="abs brand" style="left:563px;top:2442px;font-size:16px;color:#fff"><span class="mark" style="width:22px;height:22px"></span>VELBRIC</div>
</section>

<!-- CLIENTS & PARTNERS -->
<section>
  <div class="abs" style="left:599px;top:2557px;width:1px;height:350px;background:#e6e6e8"></div>
  <div class="abs title" style="left:200px;width:422px;text-align:center;top:2612px;font-size:27px">Our Clients</div>
  <div class="abs title" style="left:578px;width:422px;text-align:center;top:2612px;font-size:27px">Our Partners</div>
  <div class="abs logos" style="left:296px;top:2688px"><span>Arvona</span><span>Pelmeric</span><span>Tandex</span><span>Roadwise</span></div>
  <div class="abs logos" style="left:677px;top:2688px"><span>Arvona</span><span>Pelmeric</span><span>Tandex</span><span>Roadwise</span></div>
  <div class="abs dots" style="left:395px;top:2842px"><i class="on"></i><i></i><i></i><i></i></div>
  <div class="abs dots" style="left:783px;top:2842px"><i class="on"></i><i></i><i></i><i></i></div>
</section>

<!-- FOOTER -->
<footer class="foot">
  <div class="abs footer-bg"></div>
  <svg class="abs" style="left:582px;top:2886px" width="36" height="36"><circle cx="18" cy="18" r="18" fill="#3fcf7c"/><path d="M12 21l6-6 6 6" stroke="#fff" stroke-width="2" fill="none"/></svg>
  <div class="abs brand" style="left:234px;top:3006px;font-size:16px;color:#fff"><span class="mark" style="width:22px;height:22px"></span>VELBRIC</div>
  <div class="abs" style="left:234px;top:3037px;width:30px;height:2px;background:var(--green)"></div>
  <p class="abs" style="left:234px;top:3049px;width:240px">Since 2011, the Velbric team has been providing professional IT services for major Canadian corporations operating in the telecommunications and financial sectors. As such, our team is highly skilled in technology integration, legacy modernization, system architecture design, application development, quality assurance, project management and more!</p>
  <div class="abs" style="left:503px;top:3004px"><h5>QUICK LINKS</h5>
    <div style="margin-top:8px"><div class="lnk">Home</div><div class="lnk">Solutions</div><div class="lnk">Services</div><div class="lnk">About Us</div><div class="lnk">Contact Us</div></div>
  </div>
  <div class="abs" style="left:619px;top:3004px;width:200px"><h5>CONTACT US</h5>
    <p style="margin-top:14px">1200 Example Avenue, Unit 7, Springfield,<br>ON Canada, Z0Z 0Z0</p>
    <p style="margin-top:8px">Phone: (555) 014-2290</p>
    <p style="margin-top:6px">Email: <span style="color:var(--green)">info@velbriclimited.example</span></p>
  </div>
  <div class="abs" style="left:841px;top:3004px"><h5>FOLLOW US</h5>
    <div style="margin-top:10px"><div class="social"><i></i>Friendlane</div><div class="social"><i></i>Chirpline</div><div class="social"><i></i>Workweb</div></div>
  </div>
  <div class="abs" style="left:234px;top:3218px;width:732px;height:1px;background:#24272d"></div>
  <div class="abs center" style="top:3248px;font-size:9.5px;color:#d8d8d8">Copyrights © 2020 Velbric Limited. All rights reserved</div>
</footer>

</body>
</html>
```